Puslishing House Needs poster Design for Medical Book

We need an advertisement desing for a medical book on cardiology named "Lumivarte" (Hypertension), which 2nd Edition we launched last August. What makes this book special is that this is the first time in history that a hypertension book has a second edition in Brazil and was written by the Vessel Studies Unit of the Austral Guild of Circulatory Medicine in comemoration in its 100 years. The two news about this book is that we sold 1000 units since we launched (which is good) and we have now an ebook version for all tablet, smartphones and readers. From this month on it is going to happen importants hypertension meetings and we want to promote this two news about this book - 1000 units sold and ebook version. We would like to see designs that use orange (the publishing house color) and communicate celebration.

Target Market(s)

Doctors Specialist from several segments like Cardiology, Endocrinology, Nephrology, Nutrition. Most of the target are man with 50 years-old.

Industry/Entity Type

Medical

Requirements
Must have
• The adverstisement must have the attached book cover and publishing house logo (Quorvane) using only the name (without the tree) or the complete logo.
Should not have
• The design should not use old-style, serif fonts like Times new Roman.

```html
<!DOCTYPE html>
<html lang="en">
<head>
<meta charset="utf-8">
<title>Lumivarte – 1000 Units Sold and E-Book Version</title>
<link rel="stylesheet" href="https://fonts.googleapis.com/css2?family=Fredoka:wght@400;600;700&family=Oswald:wght@600;700&family=Roboto+Condensed:wght@500;700&display=swap">
<style>
  :root {
    --orange-light: #f9a12e;
    --orange: #f58b22;
    --orange-deep: #ee6e1c;
    --splash-yellow: #fcc531;
    --splash-red: #e3241c;
    --white: #ffffff;
    --cover-green-dark: #1f4a3a;
    --cover-green: #4f8a6b;
    --cover-pale: #e8eeea;
    --cover-red: #d9261c;
    --cover-grey: #6f7a7c;
    --ink: #2a2a2a;
    --brand-orange: #e6811f;
    --brand-navy: #1d2f6b;
  }
  * { margin: 0; padding: 0; box-sizing: border-box; }
  html, body { width: 847px; height: 1200px; overflow: hidden; }
  body { background: var(--orange); font-family: "Fredoka", sans-serif; }

  .poster {
    position: relative;
    width: 847px;
    height: 1200px;
    overflow: hidden;
    background: radial-gradient(ellipse at 45% 50%, var(--orange-light) 0%, var(--orange) 55%, var(--orange-deep) 100%);
  }

  .headline {
    position: absolute;
    left: 371px;
    top: 50px;
    color: var(--white);
    line-height: 1;
    text-transform: uppercase;
  }
  .headline__count { display: block; font-size: 68px; font-weight: 700; letter-spacing: 1px; }
  .headline__sold { display: block; font-size: 64px; font-weight: 600; margin-top: 2px; }
  .headline__and { font-weight: 400; font-size: 58px; }
  .headline__ebook { display: block; font-size: 41px; font-weight: 600; margin-top: 6px; letter-spacing: 0.5px; }

  .splash {
    position: absolute;
    left: 70px;
    top: 60px;
    width: 640px;
    height: 950px;
    border-radius: 46% 54% 40% 60% / 45% 40% 60% 55%;
    background:
      radial-gradient(ellipse at 65% 48%, rgba(252,197,49,0.9) 0%, rgba(252,197,49,0) 45%),
      radial-gradient(ellipse at 35% 78%, rgba(227,36,28,0.9) 0%, rgba(227,36,28,0) 40%),
      radial-gradient(ellipse at 30% 25%, rgba(60,160,190,0.35) 0%, rgba(60,160,190,0) 35%);
  }

  .book {
    position: absolute;
    left: 268px;
    top: 370px;
    width: 336px;
    height: 492px;
    transform: rotate(4deg);
    background: var(--orange-deep);
    padding: 8px;
    clip-path: polygon(0 0, 100% 0, 100% 84%, 84% 100%, 0 100%);
    box-shadow: 0 6px 18px rgba(0,0,0,0.3);
  }
  .book__cover {
    position: relative;
    width: 100%;
    height: 100%;
    background: var(--cover-pale);
    clip-path: polygon(0 0, 100% 0, 100% 84%, 84% 100%, 0 100%);
    overflow: hidden;
  }
  .book__top-art {
    position: absolute;
    inset: 0 0 62% 0;
    background: linear-gradient(160deg, var(--cover-green-dark) 0%, var(--cover-green) 60%, var(--cover-pale) 100%);
  }
  .book__dot {
    position: absolute;
    left: 32px; top: 52px;
    width: 26px; height: 26px;
    border-radius: 50%;
    background: var(--white);
  }
  .book__authors {
    position: absolute;
    left: 88px; top: 44px;
    list-style: none;
    font-family: "Roboto Condensed", sans-serif;
    font-weight: 700;
    font-size: 17px;
    line-height: 1.35;
    color: var(--white);
  }
  .book__title {
    position: absolute;
    left: 40px; top: 196px;
    font-family: "Oswald", sans-serif;
    font-weight: 700;
    font-size: 50px;
    letter-spacing: 1px;
    color: var(--cover-red);
    text-transform: uppercase;
    line-height: 1;
  }
  .book__bottom-art {
    position: absolute;
    left: 0; right: 0; top: 62%; bottom: 0;
    background: linear-gradient(180deg, var(--cover-pale) 0%, #c9d1d0 50%, var(--cover-grey) 100%);
  }
  .book__publisher {
    position: absolute;
    left: 22px; bottom: 22px;
    width: 26px; height: 30px;
    background: var(--white);
    border: 1px solid var(--cover-grey);
  }
  .book__edition {
    position: absolute;
    left: 60px; bottom: 24px;
    font-family: "Roboto Condensed", sans-serif;
    font-weight: 500;
    font-size: 12px;
    color: var(--ink);
  }
  .book__badge {
    position: absolute;
    bottom: 60px;
    width: 24px; height: 24px;
    border-radius: 50%;
  }
  .book__badge--one { right: 66px; background: #3a6fb0; }
  .book__badge--two { right: 36px; background: var(--cover-red); }

  .partners {
    position: absolute;
    left: 0; top: 1037px;
    width: 847px;
    height: 143px;
    background: var(--white);
    display: flex;
    align-items: center;
    justify-content: space-around;
    padding: 0 40px;
  }
  .partner {
    display: flex;
    align-items: center;
    gap: 8px;
    font-family: "Fredoka", sans-serif;
    font-weight: 600;
    font-size: 22px;
  }
  .partner__mark { width: 22px; height: 22px; }
  .partner--quorvane { color: var(--brand-orange); }
  .partner--quorvane .partner__mark { background: var(--brand-orange); }
  .partner--fecundo { color: var(--ink); }
  .partner--fecundo .partner__mark { background: #c9a94a; }
  .partner--brisante { color: var(--ink); }
  .partner--brisante .partner__mark { background: var(--ink); }
  .partner--vereda { color: var(--brand-navy); }
  .partner--vereda .partner__mark { background: var(--splash-red); border-radius: 50%; }

  .footer-strip {
    position: absolute;
    left: 0; bottom: 0;
    width: 847px;
    height: 20px;
    background: var(--orange-deep);
  }
</style>
</head>
<body>
<main class="poster">
  <div class="splash" role="img" aria-label="Celebratory paint splash in yellow, orange and red with swirling coloured ribbons and butterflies"></div>

  <h1 class="headline">
    <span class="headline__count">1000 Units</span>
    <span class="headline__sold">Sold <span class="headline__and">and</span></span>
    <span class="headline__ebook">E - Book Version</span>
  </h1>

  <div class="book">
    <div class="book__cover">
      <div class="book__top-art" role="img" aria-label="Dark green abstract cover artwork"></div>
      <span class="book__dot"></span>
      <ul class="book__authors">
        <li>Lívia R. Castanho</li>
        <li>Teodoro Vasques</li>
        <li>Marcelo Ilharco</li>
      </ul>
      <div class="book__bottom-art" role="img" aria-label="Photograph of a blood pressure gauge and bulb"></div>
      <h2 class="book__title">Lumivarte</h2>
      <span class="book__badge book__badge--one"></span>
      <span class="book__badge book__badge--two"></span>
      <span class="book__publisher"></span>
      <span class="book__edition">2ª EDIÇÃO</span>
    </div>
  </div>

  <footer class="partners">
    <div class="partner partner--quorvane"><span class="partner__mark"></span>Quorvane</div>
    <div class="partner partner--fecundo"><span class="partner__mark"></span>Fecundo Editora</div>
    <div class="partner partner--brisante"><span class="partner__mark"></span>Brisante</div>
    <div class="partner partner--vereda"><span class="partner__mark"></span>Editora Vereda</div>
  </footer>
  <div class="footer-strip"></div>
</main>
</body>
</html>
```